Website for Brackley Fabrication & Construction Ltd

General Note to all.

1. Piling and gas works are separate areas of work and should not be put together.
- the marine section should really be the piling works and should have all the barges/water piles etc.
- the gas section should have the big silo looking thing

2. I would like to add in Specialist Onsite Labour and Management in the 'our services' section. The would include the Supervisors, Coded Welders, Site Fitters and Crane and Rig Crews etc.

3. I did like it how someone had use the BFC header logo as the top of the webpage with the individual tabs above and the website starting below. Please remove the VAT number and phone number from this section.

4. I also liked how one designer incorporate the orange line with spark (from the logo) as a page separator representing the welding part of the business

5. Add in a Mission Statement - To go above and beyond in to ensure our clients projects are delivered safely, ahead of schedule, in any environment for the benefit of not only our customers but also our employees and communities we work in.

6. Add in Business Objectives -BFC is on a mission to be one of the leading contractors in UK to supply All Site Labour - ranging from Site Management, fully Coded Welders, Site Fitters and Crane and Rig Crews.

7. I am happy for you to add in photos that are not ours for the thumbs nails for the our services. ie a colourful welding pics/cool tunnelling pic etc - just make sure I will not get done for copy write infringements

8. I would like a some type of 'contact us' field or 'request a consultation' section.

9. Please confirm if the webpages you create will be compatible for both desktop and mobile app and how difficult it will be to update personally once it is live.

10. You have all done very well and have thus far been very impressed with what you have produced. I gave a very vague brief as I was not entirely sure how you would go about making something with very little information. Some of the designs look very professional.

11. I'm not sure how once I choose the winning design how that then transfers over to my domain? Perhaps someone can help me with that? I will also be looking for a web hosting platform so feel free to provide this information.

After using Sketch hive for successful getting a professional logo for the company I'm giving the web design option a go.

I am looking for a professional website for the above civil construction company.

The company director has many years experience in Marine, tunnelling, conveyors, stadium construction gas and piling works including piling works for coal ports, bridges and tunnels.

The company currently provide 20+ skilled and experienced guys from all trades (supervisors, coded welders, fitters, crane drivers and crane supervisors, rigglers, slingers and piling operatives) on the Corran Flowpath project in London - London's new super sewer. Most of this work is off barges carrying cranes (upto 600T and drill rigs).

As we are looking to expand and get more subcontracts we need a web presence to say who we are and what we do.

I'll include the 2 company logos we currently use below

I have included an info doc with pics you may or may not use.

Target Market(s)

Mainly other large construction companies and potential subcontractors

Industry/Entity Type

Construction Company

Coding

Coded - Design and coding required

Font styles to use
Sans Serif

Colors
0655a3
f37122
ffffff

Requirements
Must have
• Few tabs
• Simple to use/update but still professional look
• The challenge will be making the website look professional with not much available content.
Should not have
• No residential house building

```html
<!DOCTYPE html>
<html lang="en">
<head>
<meta charset="utf-8">
<title>Brackley Fabrication &amp; Construction Ltd</title>
<link href="https://fonts.googleapis.com/css2?family=Poppins:wght@300;400;500;600;700&display=swap" rel="stylesheet">
<style>
:root{
  --blue:#0655a3;
  --navy:#134579;
  --navy-dark:#0d3560;
  --orange:#f37122;
  --white:#ffffff;
  --grey-bg:#ececec;
  --text:#555;
  --heading:#222;
}
*{margin:0;padding:0;box-sizing:border-box}
html,body{width:1200px;height:2991px;overflow:hidden}
body{font-family:"Poppins",sans-serif;color:var(--text);background:var(--white);position:relative}

/* header */
.site-header{position:absolute;top:0;left:0;width:1200px;height:92px;background:var(--white);z-index:3;border-bottom:3px solid var(--orange)}
.nav-link{position:absolute;top:58px;font-size:12px;color:var(--navy);font-weight:500}
.brand{position:absolute;left:505px;top:8px;width:130px;height:84px;display:flex;align-items:center;justify-content:center;gap:6px}
.brand-dot{width:14px;height:14px;border-radius:50%;background:var(--orange)}
.brand-name{font-size:30px;font-weight:700;color:var(--navy);letter-spacing:1px}

/* hero */
.hero{position:absolute;top:92px;left:0;width:1200px;height:500px;overflow:hidden}
.hero-photo{position:absolute;inset:0;background:linear-gradient(90deg,#f4f6f9 0%,#dfe6ee 45%,#a7b9cf 70%,#7e95b3 100%)}
.hero-title{position:absolute;left:135px;top:130px;font-size:24px;font-weight:700;color:var(--navy)}
.hero-text{position:absolute;left:137px;top:176px;width:540px;font-size:12.5px;line-height:23px;color:#333}
.btn{display:inline-block;background:var(--orange);color:var(--white);font-weight:600;font-size:11px;text-transform:uppercase;border-radius:18px;text-align:center}
.hero-btn{position:absolute;left:133px;top:266px;width:144px;height:34px;line-height:34px}
.slider-dots{position:absolute;left:1064px;top:155px}
.slider-dots span{display:block;width:7px;height:7px;border-radius:50%;background:#c9d3df;margin-bottom:14px}
.slider-dots span.active{background:var(--navy)}
.hero-curve{position:absolute;top:520px;left:0;z-index:2}

/* welcome */
.section-title{font-size:15px;font-weight:700;color:var(--heading);text-transform:uppercase;text-align:center}
.section-title em{font-style:normal;color:var(--orange)}
.welcome .section-title{position:absolute;top:630px;width:1200px}
.welcome-text{position:absolute;top:660px;left:180px;width:840px;text-align:center;font-size:10px;line-height:18px;color:#666}
.welcome-text p{margin-bottom:8px}
.welcome-text .objectives strong{color:var(--navy);font-weight:600}

/* services */
.services{position:absolute;top:835px;left:0;width:1200px;height:393px;background:var(--grey-bg)}
.services .section-title{position:absolute;top:38px;width:1200px}
.services-intro{position:absolute;top:70px;left:340px;width:520px;text-align:center;font-size:10px;line-height:20px;color:#777}
.view-link{font-size:10px;color:var(--orange);text-decoration:underline}
.services-link{position:absolute;top:115px;width:1200px;text-align:center}
.service{position:absolute;top:172px;width:150px;height:150px;border-radius:50%;overflow:hidden}
.service-label{position:absolute;bottom:20px;width:100%;text-align:center;font-size:9.5px;font-weight:700;color:var(--white);text-transform:uppercase;line-height:12px}
.service.featured{background:var(--navy)}
.service.featured .service-label{top:42px;bottom:auto}
.service-desc{position:absolute;top:62px;width:100%;text-align:center;font-size:8.5px;color:#dfe7f1;line-height:14px}
.service .small-btn{position:absolute;top:100px;left:48px;width:54px;height:16px;line-height:16px;font-size:7px;text-transform:none}

/* CEO */
.ceo-photo{position:absolute;left:160px;top:1255px;width:295px;height:350px;background:linear-gradient(180deg,#e5e5e5,#9a9a9a 60%,#2d2d2d)}
.ceo-label{position:absolute;left:533px;top:1290px;font-size:9px;font-weight:700;color:var(--orange);text-transform:uppercase}
.ceo-name{position:absolute;left:533px;top:1315px;font-size:14px;font-weight:700;color:var(--heading);text-transform:uppercase}
.ceo-text{position:absolute;left:533px;top:1345px;width:500px;font-size:10px;line-height:19px;color:#666}
.ceo-text p{margin-bottom:12px}
.ceo-btn{position:absolute;left:533px;top:1530px;width:146px;height:34px;line-height:34px;text-transform:none;font-weight:500}

/* projects */
.projects{position:absolute;top:1605px;left:0;width:1200px;height:195px;background:linear-gradient(180deg,#1c4f86,#174577)}
.projects .section-title{position:absolute;top:75px;width:1200px;color:var(--white)}
.filters{position:absolute;top:122px;width:1200px;text-align:center;font-size:11px;color:#cfdcec}
.filters span{margin:0 10px}
.filters .current{color:var(--white);font-weight:600}
.tile{position:absolute;width:300px;height:186px}
.tile-caption{position:absolute;left:0;bottom:0;width:100%;height:40px;background:rgba(0,0,0,.35);display:flex;align-items:center;justify-content:space-between;padding:0 22px;color:var(--white);font-size:10px;font-weight:600}
.tile-caption .btn{background:rgba(255,255,255,.85);color:#333;text-transform:none;font-weight:500;font-size:9px;width:54px;height:20px;line-height:20px}

/* team */
.team-title{position:absolute;left:142px;top:2257px;font-size:14px;font-weight:700;color:var(--heading);text-transform:uppercase;line-height:20px}
.team-title em{font-style:normal;color:var(--orange);display:block}
.team-text{position:absolute;left:142px;top:2305px;width:200px;font-size:10px;line-height:17px;color:#666}
.team-link{position:absolute;left:145px;top:2372px}
.member{position:absolute;top:2252px;width:132px;height:170px}
.member-role{position:absolute;top:2430px;width:132px;text-align:center;font-size:9px;color:#333;text-transform:uppercase}

/* footer */
.skyline{position:absolute;top:2500px;left:0;width:1200px;height:72px;background:linear-gradient(180deg,rgba(19,69,121,0) 0%,rgba(19,69,121,.35) 40%,#134579 100%)}
.site-footer{position:absolute;top:2570px;left:0;width:1200px;height:380px;background:var(--navy)}
.footer-heading{position:absolute;top:68px;font-size:11px;font-weight:600;color:var(--white);text-transform:uppercase}
.footer-list{position:absolute;top:92px;list-style:none;font-size:10px;line-height:24px;color:#d8e2ee}
.contact-row{position:absolute;display:flex;gap:14px;font-size:10px;line-height:18px;color:#d8e2ee}
.contact-row svg{flex:none;margin-top:2px}
.social{position:absolute;top:100px;left:567px;display:flex;gap:10px}
.social span{width:16px;height:16px;border-radius:50%;background:#4d7eb4}
.field{position:absolute;left:806px;width:245px;height:34px;border:1px solid #6f93bd;font-size:9px;color:#93aecd;padding:10px 10px}
.send{position:absolute;left:806px;top:295px;width:62px;height:26px;border:1px solid #6f93bd;font-size:9px;color:var(--white);display:flex;align-items:center;justify-content:center;gap:6px}
.footer-bar{position:absolute;top:2950px;left:0;width:1200px;height:41px;background:var(--navy-dark);font-size:9px;color:#9fb4cd;padding:14px 140px}
</style>
</head>
<body>

<header class="site-header">
  <a class="nav-link" style="left:158px">Home</a>
  <a class="nav-link" style="left:233px">About us</a>
  <a class="nav-link" style="left:318px">What we do</a>
  <a class="nav-link" style="left:424px">Services</a>
  <div class="brand"><span class="brand-dot"></span><span class="brand-name">BFC</span></div>
  <a class="nav-link" style="left:703px">Our Projects</a>
  <a class="nav-link" style="left:814px">Our Team</a>
  <a class="nav-link" style="left:908px">Blog</a>
  <a class="nav-link" style="left:974px">Contact us</a>
</header>

<section class="hero">
  <div class="hero-photo" role="img" aria-label="Smiling construction workers in hard hats and checked shirts on a building site"></div>
  <h1 class="hero-title">OUR MISSION STATEMENT</h1>
  <p class="hero-text">To go above and beyond in to ensure our clients projects are delivered safely, ahead of schedule, in any environment for the benefit of not only our customers but also our employees and communities we work in.</p>
  <a class="btn hero-btn">Contact us</a>
  <div class="slider-dots"><span></span><span class="active"></span><span></span><span></span></div>
</section>
<svg class="hero-curve" width="1200" height="80" viewBox="0 0 1200 80">
  <path d="M0 20 Q600 110 1200 10 L1200 80 L0 80 Z" fill="#fff"/>
  <path d="M0 28 Q600 106 1200 16" fill="none" stroke="#f37122" stroke-width="5"/>
  <path d="M0 22 Q600 98 1200 10" fill="none" stroke="#0655a3" stroke-width="2"/>
</svg>

<section class="welcome">
  <h2 class="section-title">Welcome to <em>Brackley Fabrication &amp; Construction</em></h2>
  <div class="welcome-text">
    <p>Brackley Fabrication &amp; Construction has over 15years experience working in the civil construction industry. We are currently working on the Corran Flowpath project in London. We are subcontracted to Halvern Marsh Joint Venture and provide a highly skilled workforce across many of the Corran Flowpath sites.</p>
    <p>We have a strong history in the piling industry both in the UK and in Australia. Notable projects include working on K7 and K10 Coal Berths with Keldon Ridge and Tallowby Bridge over the Warrin River for Carrowgate in NSW Australia.</p>
    <p class="objectives"><strong>Business Objectives:</strong> BFC is on a mission to be one of the leading contractors in UK to supply All Site Labour - ranging from Site Management, fully Coded Welders, Site Fitters and Crane and Rig Crews.</p>
  </div>
</section>

<section class="services">
  <h2 class="section-title">Services <em>we provide</em></h2>
  <p class="services-intro">Brackley Fabrication &amp; Construction is a leading provider of diversified services to the resources, energy, civil infrastructure and urban development sectors.</p>
  <div class="services-link"><a class="view-link">View All Services</a></div>
  <div class="service" style="left:80px;background:linear-gradient(180deg,#b9d3ec,#8b8a7f 60%,#3e5068)" role="img" aria-label="Conveyor structure on a bulk materials site"><span class="service-label">Conveyors</span></div>
  <div class="service" style="left:258px;background:linear-gradient(180deg,#a9c6e6,#b77a52 60%,#3e5068)" role="img" aria-label="Stadium under construction"><span class="service-label">Stadium<br>Construction</span></div>
  <div class="service featured" style="left:436px"><span class="service-label">Tunnelling</span><p class="service-desc">Lorem ipsum dolor sit amet,<br>consectetuer elit.</p><a class="btn small-btn">Read More</a></div>
  <div class="service" style="left:614px;background:linear-gradient(180deg,#c8d6e4,#9a9a94 60%,#3e5068)" role="img" aria-label="Large gas storage silo"><span class="service-label">Gas<br>Works</span></div>
  <div class="service" style="left:792px;background:linear-gradient(180deg,#9fbfdc,#5d6f78 60%,#2e4560)" role="img" aria-label="Piling barges and water piles on a river"><span class="service-label">Piling<br>Works</span></div>
  <div class="service" style="left:970px;background:linear-gradient(180deg,#f0c36a,#c0392b 60%,#2c3e66)" role="img" aria-label="Site crew of welders, fitters and supervisors"><span class="service-label">Specialist Onsite<br>Labour &amp; Management</span></div>
</section>

<section class="ceo">
  <div class="ceo-photo" role="img" aria-label="Portrait of the company director in a dark suit, arms crossed"></div>
  <p class="ceo-label">Word about CEO</p>
  <h3 class="ceo-name">Daniel Harwood</h3>
  <div class="ceo-text">
    <p>Daniel Harwood was born and raised in South East London. After finishing school he completed a Welding and Fabrication apprenticeship with Arlow Welders and Stanmore Civils. During this time he gained a lot of experience in structural steel welding becoming a coded welder and working on both the Riverside and Northgate stadiums.</p>
    <p>Soon after completing his apprenticeship he moved over to Australia and was fortunate to work for some of the most prestigious civil construction companies: Keldon Ridge, Pellbrook and Carrowgate. Here he was also able to gain additional qualifications in Rigging and Open Crane Operating making him an exceptional all-rounder on sites.</p>
  </div>
  <a class="btn ceo-btn">know more about him</a>
</section>

<section class="projects" role="img" aria-label="Faint waterfront construction scene behind the projects heading">
  <h2 class="section-title">Latest Projects</h2>
  <div class="filters"><span class="current">All</span><span>Conveyors</span><span>Stadium Construction</span><span>Tunnelling</span><span>Gas Works</span><span>Piling Works</span><span>Bridges</span></div>
</section>
<div class="tile" style="left:0;top:1800px;background:linear-gradient(180deg,#7fa9d8,#a9abaa 60%,#6f6b66)" role="img" aria-label="Bridge beam being lifted into place"></div>
<div class="tile" style="left:300px;top:1800px;background:linear-gradient(180deg,#a9c3dc,#6c4a33 60%,#4b5b6b)" role="img" aria-label="Steel sheet piles along a river"></div>
<div class="tile" style="left:600px;top:1800px;background:linear-gradient(180deg,#c9d4dd,#b34a3a 55%,#6f6b68)" role="img" aria-label="Red cranes on a marine site"></div>
<div class="tile" style="left:900px;top:1800px;background:linear-gradient(180deg,#7ea5d2,#b35a3a 55%,#4d4a45)" role="img" aria-label="Barge with piling rig"></div>
<div class="tile" style="left:0;top:1986px;background:linear-gradient(180deg,#8fb3d8,#4f5b55 60%,#3c4a55)" role="img" aria-label="Jack-up barges on the river"></div>
<div class="tile" style="left:300px;top:1986px;background:linear-gradient(180deg,#b3c2cf,#8a4a3e 55%,#55504a)" role="img" aria-label="Crawler crane at a riverside site"></div>
<div class="tile" style="left:600px;top:1986px;background:linear-gradient(180deg,#6f8fc0,#a07a5a 55%,#3c3a45)" role="img" aria-label="Sewer works at dusk"><div class="tile-caption"><span>London's new 'super sewer'</span><span class="btn">Details</span></div></div>
<div class="tile" style="left:900px;top:1986px;background:linear-gradient(180deg,#6f9bd0,#b9c4cf 60%,#55636f)" role="img" aria-label="Tall cranes over a harbour"></div>

<section class="team">
  <h2 class="team-title">Awesome <em>Team</em></h2>
  <p class="team-text">Lorem ipsum dolor sit amet, consectetuer adipiscing elit. Aenean commodo ligula eget dolor.</p>
  <a class="view-link team-link">view all</a>
  <div class="member" style="left:417px;background:linear-gradient(135deg,#f0a030,#c0392b 55%,#2c3e66)" role="img" aria-label="Welder at work with sparks"></div>
  <div class="member" style="left:585px;background:linear-gradient(180deg,#d9c08a,#8a7a5a 60%,#3d4a5c)" role="img" aria-label="Site fitter on a steel structure"></div>
  <div class="member" style="left:760px;background:linear-gradient(180deg,#b9cde2,#c0392b 60%,#6a3a3a)" role="img" aria-label="Rig crew in red overalls"></div>
  <div class="member" style="left:935px;background:linear-gradient(180deg,#e6eaf0,#d7e34a 65%,#8a9a3a)" role="img" aria-label="Site supervisor in hard hat and hi-vis vest"></div>
  <p class="member-role" style="left:417px">Coded Welders</p>
  <p class="member-role" style="left:585px">Site Fitters</p>
  <p class="member-role" style="left:760px">Rig Crews</p>
  <p class="member-role" style="left:935px">Supervisors</p>
</section>

<div class="skyline" role="img" aria-label="City skyline silhouette with bridge"></div>

<footer class="site-footer">
  <h4 class="footer-heading" style="left:150px">Quick Links</h4>
  <ul class="footer-list" style="left:150px">
    <li>Home</li><li>About us</li><li>What we do</li><li>Services we offer</li><li>Projects</li><li>Blog</li><li>Contact us</li>
  </ul>
  <h4 class="footer-heading" style="left:350px">Contact us</h4>
  <div class="contact-row" style="left:352px;top:92px">
    <svg width="12" height="16" viewBox="0 0 12 16"><path d="M6 0a6 6 0 0 0-6 6c0 4.5 6 10 6 10s6-5.5 6-10a6 6 0 0 0-6-6zm0 8.5A2.5 2.5 0 1 1 6 3.5a2.5 2.5 0 0 1 0 5z" fill="#d8e2ee"/></svg>
    <span>418 Harbour Road<br>Eastmere, QX 20417</span>
  </div>
  <div class="contact-row" style="left:352px;top:158px">
    <svg width="12" height="12" viewBox="0 0 12 12"><path d="M2.5 0l2 3-1.2 1.4a7 7 0 0 0 4.3 4.3L9 7.5l3 2-1 2.5C5 12 0 7 0 1z" fill="#d8e2ee"/></svg>
    <span>+44 000 123 4567</span>
  </div>
  <div class="contact-row" style="left:352px;top:210px">
    <svg width="14" height="10" viewBox="0 0 14 10"><rect width="14" height="10" fill="#d8e2ee"/><path d="M0 0l7 5 7-5" fill="none" stroke="#134579" stroke-width="1.2"/></svg>
    <span>contact@bfc.example<br>info@bfc.example</span>
  </div>
  <h4 class="footer-heading" style="left:567px">Social Links</h4>
  <div class="social"><span></span><span></span><span></span><span></span></div>
  <h4 class="footer-heading" style="left:806px">Get in touch</h4>
  <div class="field" style="top:95px">Name</div>
  <div class="field" style="top:142px">Phone</div>
  <div class="field" style="top:188px">Email</div>
  <div class="field" style="top:236px;height:50px">Message</div>
  <div class="send">SEND <svg width="10" height="10" viewBox="0 0 10 10"><path d="M0 4l10-4-4 10-1.5-4.5z" fill="#f37122"/></svg></div>
</footer>
<div class="footer-bar">©2018 bfc.example, All Rights Reserved</div>

</body>
</html>
```